Wheelchair Accessible Accommodation

We are 100% online, promoting accommodation details and booking facilities for wheelchair dependant travellers.
Listings will only be accommodation providers which meet our specific criteria.

Target Market(s)

Wheelchair dependant people and their companions

Industry/Entity Type

Accommodation

Contact Information for Business Card

Name, mobile phone number, email address, website address

```html
<!DOCTYPE html>
<html lang="en">
<head>
<meta charset="utf-8">
<title>Level Path Lodging – Business Card</title>
<link href="https://fonts.googleapis.com/css2?family=Lato:wght@400;700;900&display=swap" rel="stylesheet">
<style>
  :root {
    --backdrop: #2a2a2a;
    --card-white: #ffffff;
    --brand-red: #e41e26;
    --card-black: #050505;
    --ink: #111111;
    --on-dark: #ffffff;
  }
  * { box-sizing: border-box; margin: 0; padding: 0; }
  html, body {
    width: 1200px;
    height: 1000px;
    overflow: hidden;
    background: var(--backdrop);
    font-family: "Lato", Arial, sans-serif;
  }
  .business-card {
    position: absolute;
    left: 150px;
    top: 240px;
    width: 900px;
    height: 520px;
    border-radius: 20px;
    overflow: hidden;
    background: var(--card-white);
    box-shadow: 0 20px 50px rgba(0,0,0,0.5);
  }
  .card-top {
    position: absolute;
    left: 0; top: 0;
    width: 100%;
    height: 318px;
    background: var(--card-white);
  }
  .accent-rule {
    position: absolute;
    left: 0; top: 318px;
    width: 100%;
    height: 9px;
    background: var(--brand-red);
  }
  .card-bottom {
    position: absolute;
    left: 0; top: 327px;
    width: 100%;
    height: 193px;
    background: var(--card-black);
  }
  .brand {
    position: absolute;
    left: 58px;
    top: 120px;
    display: flex;
    align-items: center;
    gap: 18px;
  }
  .brand-dot {
    width: 64px;
    height: 64px;
    border-radius: 50%;
    background: var(--brand-red);
    flex: none;
  }
  .brand-name {
    font-weight: 900;
    font-size: 46px;
    line-height: 1.02;
    color: var(--brand-red);
    letter-spacing: -0.5px;
  }
  .holder-name {
    position: absolute;
    left: 585px;
    top: 138px;
    font-weight: 700;
    font-size: 29px;
    color: var(--ink);
  }
  .contact-list {
    position: absolute;
    left: 58px;
    top: 352px;
    list-style: none;
  }
  .contact-item {
    display: flex;
    align-items: center;
    gap: 28px;
    height: 48px;
    color: var(--on-dark);
    font-weight: 700;
    font-size: 26px;
    letter-spacing: 1.2px;
  }
  .contact-icon {
    width: 34px;
    height: 34px;
    flex: none;
  }
</style>
</head>
<body>
  <div class="business-card">
    <div class="card-top"></div>
    <div class="accent-rule"></div>
    <div class="card-bottom"></div>

    <div class="brand">
      <span class="brand-dot"></span>
      <span class="brand-name">Level Path<br>Lodging</span>
    </div>

    <p class="holder-name">Daniel Harwood</p>

    <ul class="contact-list">
      <li class="contact-item">
        <svg class="contact-icon" viewBox="0 0 34 34" aria-hidden="true">
          <circle cx="17" cy="17" r="17" fill="var(--brand-red)"/>
          <path d="M11.5 9.5c1-.6 2-.4 2.6.5l1.6 2.6c.5.8.3 1.7-.4 2.3l-1 .8c.9 2 2.4 3.5 4.4 4.4l.8-1c.6-.7 1.5-.9 2.3-.4l2.6 1.6c.9.6 1.1 1.6.5 2.6l-.8 1.2c-.8 1.2-2.3 1.6-3.7 1.1-4.8-1.8-8.6-5.6-10.4-10.4-.5-1.4-.1-2.9 1.1-3.7z" fill="var(--on-dark)"/>
        </svg>
        <span>[+61] 0400 123 456</span>
      </li>
      <li class="contact-item">
        <svg class="contact-icon" viewBox="0 0 34 34" aria-hidden="true">
          <circle cx="17" cy="17" r="17" fill="var(--brand-red)"/>
          <rect x="8" y="11" width="18" height="12.5" rx="1.5" fill="var(--on-dark)"/>
          <path d="M8.5 11.8 17 18.2l8.5-6.4" fill="none" stroke="var(--brand-red)" stroke-width="1.6"/>
        </svg>
        <span>stay@levelpathonline.com.au</span>
      </li>
      <li class="contact-item">
        <svg class="contact-icon" viewBox="0 0 34 34" aria-hidden="true">
          <circle cx="17" cy="17" r="17" fill="var(--brand-red)"/>
          <g fill="none" stroke="var(--on-dark)" stroke-width="1.6">
            <circle cx="17" cy="17" r="9"/>
            <ellipse cx="17" cy="17" rx="4" ry="9"/>
            <path d="M8 17h18M9.5 12.5h15M9.5 21.5h15"/>
          </g>
        </svg>
        <span>www.levelpathonline.com.au</span>
      </li>
    </ul>
  </div>
</body>
</html>
```